Have Logo - Need Business Card Design!!!

I am looking for a business card design for a real estate development business. The company name is Orvane Realty Partners. I already have a logo created by Pixel Harbor and would like this logo to be incorporated into the design. I have uploaded the files. The card needs to be professional, but visually interesting. Not necessary to be double-sided, but if you want to get creative and can think of something to put on the back then have at it.

Target Market(s)

The target audience for these business cards will be professionals in the real estate industry.

Industry/Entity Type

Real Estate

Requirements
Must have
• The business card must have all the necessary items for a business card, i.e. company name, our logo, name (however, not title necessary), office address, office phone number, cell number, fax number, website address, etc.

You can use the information below for the card:

Martin R. Oswell
812 Linden Avenue
San Francisco, California 94177

www.orvanerealtypartners.example
moswell@orvanerealtypartners.example
Office: 415-555-0143
Fax: 415-555-0147
Cell: 415-555-0182

```html
<!DOCTYPE html>
<html lang="en">
<head>
<meta charset="utf-8">
<title>Orvane Realty Partners – Business Card</title>
<link rel="stylesheet" href="https://fonts.googleapis.com/css2?family=Arimo:wght@400;700&display=swap">
<style>
  :root {
    --stage: #3b3b3d;
    --navy: #1c3473;
    --navy-light: #2f57a6;
    --green: #1f8a3c;
    --ink: #4a4a4a;
    --rule: #b9b9b9;
    --paper: #ffffff;
    --paper-shade: #eceff3;
  }
  * { box-sizing: border-box; margin: 0; padding: 0; }
  html, body {
    width: 1200px; height: 871px; overflow: hidden;
    background: var(--stage);
    font-family: "Arimo", Arial, sans-serif;
  }
  .stage { position: relative; width: 1200px; height: 871px; }
  .card {
    position: absolute; left: 280px;
    width: 640px; height: 366px;
    border-radius: 18px; overflow: hidden;
    box-shadow: 0 10px 30px rgba(0,0,0,.45);
  }

  /* Back */
  .card-back {
    top: 40px;
    background: linear-gradient(160deg, var(--navy-light) 0%, var(--navy) 70%);
    color: var(--paper);
    display: flex; flex-direction: column; align-items: center; justify-content: center;
  }
  .back-brand { display: flex; align-items: center; gap: 14px; margin: 40px 0 90px; }
  .back-brand .mark-square { width: 34px; height: 34px; background: var(--paper); }
  .back-brand .brand-name { font-size: 26px; font-weight: 400; letter-spacing: 1px; }
  .back-web { font-size: 18px; letter-spacing: 5px; }

  /* Front */
  .card-front {
    top: 446px;
    background: linear-gradient(180deg, var(--paper) 0%, var(--paper) 55%, var(--paper-shade) 100%);
  }
  .front-brand {
    position: absolute; left: 36px; top: 118px;
    display: flex; align-items: center; gap: 12px;
  }
  .front-brand .mark-square { width: 30px; height: 30px; background: var(--green); }
  .front-brand .brand-name { color: var(--green); font-size: 25px; font-weight: 400; line-height: 1.1; }
  .divider { position: absolute; left: 300px; top: 50px; width: 1px; height: 200px; background: var(--rule); }
  .contact {
    position: absolute; left: 320px; top: 52px; width: 296px;
    color: var(--ink); font-size: 13px; line-height: 1.45;
  }
  .contact .person { color: var(--green); font-size: 21px; margin-bottom: 16px; }
  .contact .address { margin-bottom: 4px; }
  .band-rule { position: absolute; left: 0; right: 0; top: 268px; height: 3px; background: var(--green); }
  .band {
    position: absolute; left: 0; right: 0; top: 276px; bottom: 0;
    background: linear-gradient(180deg, var(--navy-light), var(--navy));
    border-top: 2px solid var(--green);
    display: flex; align-items: center; justify-content: center;
  }
  .band .web { color: var(--paper); font-size: 18px; letter-spacing: 5px; }
</style>
</head>
<body>
<main class="stage">
  <section class="card card-back" aria-label="Card back">
    <div class="back-brand">
      <span class="mark-square"></span>
      <span class="brand-name">Orvane Realty Partners</span>
    </div>
    <p class="back-web">www.orvanerealtypartners.example</p>
  </section>

  <section class="card card-front" aria-label="Card front">
    <div class="front-brand">
      <span class="mark-square"></span>
      <span class="brand-name">Orvane Realty<br>Partners</span>
    </div>
    <div class="divider"></div>
    <div class="contact">
      <p class="person">Martin R. Oswell</p>
      <p class="address">812 Linden Avenue<br>San Francisco, California 94177</p>
      <p>P : 415-555-0143</p>
      <p>C : 415-555-0182</p>
      <p>F : 415-555-0147</p>
      <p>E : moswell@orvanerealtypartners.example</p>
    </div>
    <div class="band-rule"></div>
    <div class="band"><p class="web">www.orvanerealtypartners.example</p></div>
  </section>
</main>
</body>
</html>
```